Create new graphics and layout for Corelume Ascent Deck

Corelume is a b2b fintech focused on identifying, refining, valuing, and monetizing data. It gives companies an opportunity to use their unused data and generate a revenue stream. We want to make pages that creatively communicate this. Additionally we want the graphics to elicit trust and brand recognition. The current capabilities deck provided does not achieve this goal so we encourage you to provide your best ideas, using the brand guidelines provided.

Please use a light or white background
Brand and Typesetting is provided in the Branding Guidelines document
Current draft is attached called Corelume Ascent Plan Oct 17 - Final (Redacted) for Pixelhive pages 1-10
VIsuals should be engaging but not too distracting.
We are open to all other images and overall design, while maintaining the brand guidelines. Please be creative but again professional and demonstrate that Corelume is a high tech, innovative and creative firm.
Subtle background images are also encouraged, as appropriate
Please do not grab images or graphics from the Corelume website and we are redoing the website and do not like for most of the graphics on that website.
We are re-doing the copy so you can use placeholder text.

```html
<!DOCTYPE html>
<html lang="en">
<head>
<meta charset="utf-8">
<title>Corelume Ascent Deck</title>
<link href="https://fonts.googleapis.com/css2?family=Lexend:wght@300;400;500;600;700;800&display=swap" rel="stylesheet">
<style>
:root{
  --page:#e4e6e9;
  --white:#ffffff;
  --ink:#1d1d22;
  --navy:#1b3392;
  --teal:#2b7683;
  --teal-soft:#e3f0f2;
  --navy-soft:#eef1fa;
  --grey:#6c727c;
  --line:#d9dde3;
}
*{box-sizing:border-box;margin:0;padding:0}
html,body{width:1200px;height:4231px;overflow:hidden;background:var(--page);font-family:"Lexend",sans-serif;color:var(--ink)}
.slide{position:absolute;left:34px;width:1131px;height:637px;background:var(--white);overflow:hidden;box-shadow:0 1px 4px rgba(0,0,0,.18)}
.abs{position:absolute}

/* arrow bullets */
.arrow-list{list-style:none;--arrow:var(--navy)}
.arrow-list li{position:relative;padding-left:28px}
.arrow-list li::before{content:"";position:absolute;left:0;top:calc(50% - 1px);width:15px;height:2px;background:var(--arrow)}
.arrow-list li::after{content:"";position:absolute;left:9px;top:calc(50% - 4px);width:6px;height:6px;border-top:2px solid var(--arrow);border-right:2px solid var(--arrow);transform:rotate(45deg)}

/* cover */
.cover{top:62px}
.cover .title{left:30px;top:172px;font-size:52px;font-weight:700;letter-spacing:.5px}
.cover .date{left:30px;top:258px;font-size:24px;font-weight:600;color:var(--navy);display:flex;align-items:center;gap:10px}
.cover .flags{left:30px;top:318px;font-size:22px;font-weight:400}
.cover .flags li{margin-bottom:20px;padding-left:36px}
.cover .flags li::before{width:20px;height:3px}
.cover .flags li::after{left:12px;width:8px;height:8px;top:calc(50% - 5px);border-width:3px}
.brand{left:733px;top:44px;display:flex;align-items:center;gap:14px}
.brand .dot{width:70px;height:70px;border-radius:50%;background:var(--navy)}
.brand .name{font-size:36px;font-weight:600;color:var(--navy);line-height:1}
.brand .sub{font-size:18px;font-weight:400;color:var(--navy)}

/* summary */
.summary{top:755px}
.summary .band{left:0;top:0;width:1131px;height:250px;background:linear-gradient(100deg,#20262e 0%,#4a4f57 45%,#2c3b49 100%)}
.summary .panel{left:90px;top:169px;width:467px;height:319px;background:var(--teal);color:#fff;padding:40px 38px}
.summary .panel h2{font-size:44px;font-weight:400;margin-bottom:18px}
.summary .panel .arrow-list{--arrow:#fff}
.summary .panel li{font-size:13.5px;margin-bottom:10px}
.summary .panel .sub{padding-left:28px;margin:24px 0 30px}
.summary h3{left:588px;top:275px;font-size:26px;font-weight:600;color:var(--navy)}
.summary .goals{left:598px;top:325px;font-size:12.5px}
.summary .goals li{margin-bottom:15px}

/* path */
.path{top:1448px}
.path .photo{left:0;top:0;width:407px;height:637px;background:linear-gradient(160deg,#3d3833,#7b6b5c 50%,#2e2a27)}
.path .cols{left:585px;top:105px;display:grid;grid-template-columns:265px 240px;row-gap:13px;font-size:16px}
.path .cols span{display:flex;align-items:center;gap:10px}
.path .cols span::before{content:"";width:12px;height:12px;border-radius:50%;background:var(--navy);flex:none}
.path .label{left:578px;font-size:18px;font-weight:600}
table{border-collapse:collapse}
.path td,.path th{border:1px solid #b9bec6;padding:1px 4px;text-align:left;font-weight:400;white-space:nowrap;font-size:10.5px;line-height:15px}
.path th{font-weight:600}
.path th.hl{background:var(--navy);color:#fff}
.path td.num{text-align:right}
.path .rev th{background:var(--navy);color:#fff;font-size:8px;line-height:11px}
.path .rev td{font-size:8px;line-height:11px}

/* market */
.market{top:2142px;background:linear-gradient(180deg,#fff 60%,#f2f5fb 100%)}
.market h2{left:0;width:1131px;top:92px;text-align:center;font-size:46px;font-weight:700}
.market .vr{width:1px;background:var(--line);top:190px;height:360px}
.market .hr{left:31px;width:1070px;height:1px;background:var(--line);top:351px}
.market .node{width:16px;height:16px;border-radius:50%;border:2px solid var(--navy);background:#fff;top:343px}
.market .node::after{content:"";position:absolute;left:3px;top:3px;width:6px;height:6px;border-radius:50%;background:var(--navy)}
.stat{width:230px}
.stat h4{font-size:24px;font-weight:600;color:var(--teal);margin-bottom:10px}
.stat p{font-size:11.5px;line-height:1.9}

/* hierarchy (light) */
.hierarchy{top:2835px;background:linear-gradient(120deg,#ffffff 0%,var(--navy-soft) 60%,var(--teal-soft) 100%)}
.hierarchy .hub{left:37px;top:219px;width:196px;height:196px;border-radius:50%;background:var(--navy);color:#fff;display:flex;align-items:center;justify-content:center;text-align:center;font-size:23px;font-weight:600;line-height:1.4;box-shadow:0 0 0 10px rgba(27,51,146,.12)}
.hierarchy .wire{background:var(--navy)}
.hierarchy .pip{width:10px;height:10px;border-radius:50%;background:var(--navy)}
.node-w{left:322px;width:197px;height:56px;background:#fff;border:2px solid var(--navy);color:var(--ink);display:flex;align-items:center;justify-content:center;font-size:13px;font-weight:500;box-shadow:0 4px 12px rgba(27,51,146,.10)}
.node-t{width:148px;height:56px;background:var(--teal);color:#fff;display:flex;align-items:center;justify-content:center;text-align:center;font-size:11px;font-weight:500;line-height:1.35;padding:0 8px;box-shadow:0 4px 12px rgba(43,118,131,.18)}

/* offices */
.offices{top:3526px}
.offices h2{left:31px;top:156px;font-size:38px;font-weight:600}
.offices h5{font-size:22px;font-weight:600;color:var(--navy)}
.offices .list{font-size:16px;line-height:34.5px}
.offices .map-us{left:560px;top:0;width:571px;height:410px;background:linear-gradient(135deg,#bfe6f2,#e9eef0 45%,#cde9f3)}
.offices .map-eu{left:560px;top:414px;width:571px;height:223px;background:linear-gradient(90deg,#eef0f2 50%,#e6e9ec 50%)}
</style>
</head>
<body>

<section class="slide cover">
  <svg class="abs" style="left:0;top:0" width="1131" height="637" role="img" aria-label="Photo of a smiling presenter leading a team meeting in a bright office">
    <defs>
      <linearGradient id="coverPhoto" x1="0" y1="0" x2="1" y2="1">
        <stop offset="0" stop-color="#e6eef2"/>
        <stop offset=".55" stop-color="#b9cbd6"/>
        <stop offset="1" stop-color="#6e7f8c"/>
      </linearGradient>
    </defs>
    <circle cx="885" cy="627" r="394" fill="url(#coverPhoto)"/>
    <path d="M 491 660 A 394 394 0 0 1 800 242" fill="none" stroke="var(--teal)" stroke-width="10"/>
  </svg>
  <div class="abs brand"><span class="dot"></span><div><div class="name">Corelume</div><div class="sub">Holdings, Inc.</div></div></div>
  <h1 class="abs title">BUSINESS PLAN</h1>
  <div class="abs date">
    <svg width="22" height="22" viewBox="0 0 22 22"><rect x="2" y="4" width="18" height="16" rx="2" fill="none" stroke="var(--navy)" stroke-width="2"/><line x1="2" y1="9" x2="20" y2="9" stroke="var(--navy)" stroke-width="2"/><line x1="7" y1="1" x2="7" y2="6" stroke="var(--navy)" stroke-width="2"/><line x1="15" y1="1" x2="15" y2="6" stroke="var(--navy)" stroke-width="2"/></svg>
    October 17th, 2022
  </div>
  <ul class="abs arrow-list flags">
    <li>CONFIDENTIONAL</li>
    <li>NOT FOR PUBLIC DISTRIBUTION</li>
    <li>PRIVILEGED INFORMATION</li>
  </ul>
</section>

<section class="slide summary">
  <div class="abs band" role="img" aria-label="Photo of business partners shaking hands over a desk"></div>
  <div class="abs panel">
    <h2>Summary</h2>
    <ul class="arrow-list">
      <li>Market Potential : SXXBn NFT Market by 2026</li>
      <li>Build an organization that will deliver</li>
    </ul>
    <ul class="arrow-list sub">
      <li>SXXM ARR by Q4 2025</li>
      <li>World-class People, Processes and Culture</li>
      <li>Sustainable, for-profit, for-cause business</li>
    </ul>
    <ul class="arrow-list"><li>Outline the schedule for 2023 planning</li></ul>
  </div>
  <h3 class="abs">Deliver results by December 31st:</h3>
  <ul class="abs arrow-list goals">
    <li>FUND RAISING: SXXM in institutional investments</li>
    <li>FUND RAISING: Potential sale of Sonari Patent for SXXM</li>
    <li>BLOCKCHAIN: Operational on Kestrel Chain by November 30 2022</li>
    <li>REVENUE: SXXM by end of 2023, SXXM by end of 2024</li>
    <li>CORPORATE STRUCTURE: That delivers SXXM</li>
    <li>PROOF OF TECHNOLOGIES: In cross-vertical use cases</li>
    <li>ECONOMIES OF SCALE: via low-risk, scalable models</li>
    <li>HIRING KEY TALENT: IN KEY AREAS OF THE BUSINESS</li>
    <li>SETS GOVERNANCE AND CADENCE: FOR THE BUSINESS</li>
  </ul>
</section>

<section class="slide path">
  <div class="abs photo" role="img" aria-label="Photo of two smiling colleagues looking at a laptop"></div>
  <svg class="abs" style="left:146px;top:92px" width="450" height="450">
    <circle cx="225" cy="225" r="225" fill="#fff"/>
    <circle cx="225" cy="225" r="197" fill="var(--navy)"/>
    <circle cx="239" cy="219" r="181" fill="var(--teal)"/>
    <text x="235" y="210" text-anchor="middle" fill="#fff" font-family="Lexend,sans-serif" font-size="56" font-weight="500">Path to</text>
    <text x="235" y="284" text-anchor="middle" fill="#fff" font-family="Lexend,sans-serif" font-size="60" font-weight="700">$150M</text>
  </svg>
  <div class="abs cols">
    <span>SXXBn IPO valuation @18x</span><span>Divisional focus</span>
    <span>ARR SXX, SXXM - SXXM</span><span>Governance Structure</span>
    <span>XX% Gross Margin</span><span>Focused Product Portfolio</span>
    <span>100 Employees</span><span>Customer Obsession</span>
    <span>Offices in USA, UK, Brazil</span><span>Winning Culture</span>
  </div>
  <div class="abs label" style="top:314px">Value 2025 (est)</div>
  <table class="abs" style="left:578px;top:357px">
    <tr><th>Rev Multiple</th><th class="hl">Value</th><th>NET ASSET VALUE</th><th>TOTAL VALUE ($Bn)</th></tr>
    <tr><td>7X</td><td class="num">$ 1,046</td><td class="num">$ 550</td><td class="num">$ 1,596</td></tr>
    <tr><td>10X</td><td class="num">$ 1,494</td><td class="num">$ 550</td><td class="num">$ 2,044</td></tr>
    <tr><td>18X</td><td class="num">$ 2,690</td><td class="num">$ 550</td><td class="num">$ 3,240</td></tr>
    <tr><td>25X</td><td class="num">$ 3,736</td><td class="num">$ 550</td><td class="num">$ 4,286</td></tr>
  </table>
  <div class="abs label" style="top:469px">Revenue</div>
  <table class="abs rev" style="left:578px;top:503px;width:303px">
    <tr><td>Year</td><th>2022</th><th>2023</th><th>2024</th><th>2025</th></tr>
    <tr><td>Revenue ($Mns)</td><td class="num">$ 0</td><td class="num">$ 16</td><td class="num">$ 68</td><td class="num">$ 149</td></tr>
  </table>
</section>

<section class="slide market">
  <h2 class="abs">Market Size</h2>
  <div class="abs vr" style="left:272px"></div>
  <div class="abs vr" style="left:578px"></div>
  <div class="abs vr" style="left:831px"></div>
  <div class="abs hr"></div>
  <span class="abs node" style="left:264px"></span>
  <span class="abs node" style="left:570px"></span>
  <span class="abs node" style="left:823px"></span>

  <div class="abs stat" style="left:31px;top:205px;width:236px"><h4>SXXBn</h4><p>Forecasted NFT market Size by 2030<br>Source: Clearview Market Research (CMR)</p></div>
  <div class="abs stat" style="left:309px;top:205px;width:250px"><h4>$147 Bn</h4><p>Forecasted size of the global NFT market by 2026 CAGR 35.27%<br>Source: fresh &amp; funded 19 July, 2022</p></div>
  <div class="abs stat" style="left:611px;top:205px"><h4>$41Bn</h4><p>NFT Market value in 2021</p></div>
  <div class="abs stat" style="left:865px;top:205px;width:240px"><h4>Trading Wallets</h4><p>Growth: 545,000 in 2020, to 28.6M in 2021</p></div>

  <div class="abs stat" style="left:31px;top:390px"><h4>$102M</h4><p>Record number of NFTs booked in transactions in a single day,<br>(in May 2021)</p></div>
  <div class="abs stat" style="left:309px;top:390px;width:250px"><h4>$700M</h4><p>Generated in gross sales of a pro league's top collectible product, which is a blockchain-based trading card system 2</p></div>
  <div class="abs stat" style="left:611px;top:390px;width:200px"><h4>23%</h4><p>NFTs are collected by 23% of Gen Y (millennials) in the United States</p></div>
</section>

<section class="slide hierarchy">
  <div class="abs wire" style="left:233px;top:316px;width:63px;height:2px"></div>
  <div class="abs wire" style="left:296px;top:34px;width:2px;height:572px"></div>
  <div class="abs wire" style="left:296px;top:34px;width:124px;height:2px"></div>
  <div class="abs wire" style="left:296px;top:604px;width:124px;height:2px"></div>
  <div class="abs wire" style="left:420px;top:34px;width:2px;height:572px"></div>
  <span class="abs pip" style="left:416px;top:44px"></span>
  <span class="abs pip" style="left:416px;top:586px"></span>
  <div class="abs hub">Product<br>Hierarchy</div>

  <div class="abs node-w" style="top:80px">Corelume Platform</div>
  <div class="abs node-t" style="left:581px;top:80px">Refinery</div>
  <div class="abs node-t" style="left:755px;top:80px">Vault</div>
  <div class="abs node-t" style="left:928px;top:80px">Exchange</div>

  <div class="abs node-w" style="top:218px">Sonari</div>
  <div class="abs node-t" style="left:581px;top:218px">Security &amp; Safety</div>
  <div class="abs node-t" style="left:755px;top:218px">Advertising &amp; Communication</div>
  <div class="abs node-t" style="left:928px;top:218px">Analysis</div>

  <div class="abs node-w" style="top:356px">FairLot</div>
  <div class="abs node-t" style="left:581px;top:356px">Mobile Application</div>
  <div class="abs node-t" style="left:755px;top:356px">Web-Based Platform</div>

  <div class="abs node-w" style="top:494px">Services and Consulting</div>
  <div class="abs node-t" style="left:581px;top:494px">Data Object Marketing</div>
  <div class="abs node-t" style="left:755px;top:494px">Data Brokerage</div>
  <div class="abs node-t" style="left:928px;top:494px">White labeling</div>
</section>

<section class="slide offices">
  <h2 class="abs">Global Offices</h2>
  <h5 class="abs" style="left:31px;top:228px">USA</h5>
  <div class="abs list" style="left:31px;top:256px">Pennsylvania<br>Connecticut<br>NYC<br>California<br>Chicago<br>Florida<br>Atlanta</div>
  <h5 class="abs" style="left:176px;top:228px">UK</h5>
  <div class="abs list" style="left:176px;top:256px">London (Exchange Court)</div>
  <h5 class="abs" style="left:176px;top:294px">Brazil</h5>
  <div class="abs list" style="left:176px;top:333px">San Paolo</div>
  <div class="abs map-us" role="img" aria-label="Map of the United States with office states highlighted"></div>
  <div class="abs map-eu" role="img" aria-label="Maps of Brazil and the United Kingdom with office regions highlighted in red"></div>
</section>

</body>
</html>
```